Corvells Finest 4 years in a row

I need a billboard that has all the attached logos and says:

Corvell's Finest Realtor 4 Years in a row!

1.75 Listing Fee

Tobias Wrenfield

410-555-0147

and somewhere very small at the bottom:

833-555-0192

2947 W Pennlow Rd, Bel Air, MD 21099

I put in the last winner just to give an idea of what I'm looking for, although I'd like to switch it up a little bit.

```html
<!DOCTYPE html>
<html lang="en">
<head>
<meta charset="utf-8">
<title>Corvell's Finest Realtor Billboard</title>
<link rel="stylesheet" href="https://fonts.googleapis.com/css2?family=Montserrat:wght@600;700&family=Roboto+Condensed:wght@800;900&display=swap">
<style>
  :root {
    --stage: #5b5b5b;
    --white: #ffffff;
    --navy: #11305e;
    --ink: #2a2a2a;
    --band-gray: #7a7a7a;
    --panel-dark: #231f20;
    --pill-gray: #6f6f6f;
    --badge-dark: #2b2b2b;
    --photo-suit: #2f3f5c;
    --photo-skin: #c99a80;
  }
  * { margin: 0; padding: 0; box-sizing: border-box; }
  html, body { width: 1131px; height: 1200px; overflow: hidden; }
  body { background: var(--stage); position: relative; font-family: "Montserrat", sans-serif; }

  .billboard {
    position: absolute; left: 30px; top: 444px;
    width: 1071px; height: 312px;
    background: var(--white);
    overflow: hidden;
    box-shadow: 0 10px 30px rgba(0,0,0,.35);
  }
  .band { position: absolute; left: 0; }
  .band--name { top: 152px; height: 70px; width: 590px; background: var(--band-gray); }
  .band--phone { top: 222px; height: 90px; width: 590px; background: var(--navy); }
  .panel-contact { position: absolute; left: 705px; top: 164px; width: 366px; height: 148px; background: var(--panel-dark); }

  .headline { position: absolute; left: 50px; top: 40px; font-family: "Roboto Condensed", sans-serif; font-weight: 900; text-transform: uppercase; line-height: 1; letter-spacing: -0.5px; white-space: nowrap; }
  .headline__top { display: block; color: var(--navy); font-size: 42px; }
  .headline__bottom { display: block; color: var(--ink); font-size: 60px; margin-top: 0; }

  .agent-name { position: absolute; left: 50px; top: 161px; color: var(--white); font-weight: 600; font-size: 40px; letter-spacing: 0.5px; text-transform: uppercase; line-height: 52px; white-space: nowrap; }
  .agent-phone { position: absolute; left: 50px; top: 226px; color: var(--white); font-weight: 600; font-size: 68px; line-height: 82px; letter-spacing: -1px; white-space: nowrap; }

  .agent-photo {
    position: absolute; left: 562px; top: 52px; width: 176px; height: 260px;
    border-radius: 60px 60px 0 0;
    background: linear-gradient(180deg, var(--photo-skin) 0%, var(--photo-skin) 26%, var(--photo-suit) 34%, var(--photo-suit) 100%);
  }

  .award-badge { position: absolute; left: 748px; top: 40px; width: 100px; height: 96px; border-radius: 50%; background: var(--badge-dark); }

  .brand { position: absolute; left: 870px; top: 58px; width: 180px; display: flex; flex-direction: column; align-items: center; gap: 10px; }
  .brand__mark { width: 34px; height: 34px; border-radius: 50%; background: var(--navy); }
  .brand__name { color: var(--navy); font-weight: 600; font-size: 22px; text-transform: uppercase; white-space: nowrap; }

  .listing-fee { position: absolute; left: 705px; width: 366px; top: 172px; text-align: center; color: var(--white); font-weight: 700; font-size: 29px; }
  .office-phone {
    position: absolute; left: 768px; top: 216px; width: 240px; height: 34px;
    border-radius: 8px; background: var(--pill-gray);
    display: flex; align-items: center; justify-content: center; gap: 6px;
    color: var(--white); font-weight: 700; font-size: 26px;
  }
  .office-phone svg { width: 17px; height: 17px; }
  .office-address { position: absolute; left: 795px; top: 262px; display: flex; align-items: center; gap: 10px; color: var(--white); font-weight: 600; font-size: 14.5px; line-height: 19px; }
  .office-address svg { width: 18px; height: 22px; }
</style>
</head>
<body>
  <section class="billboard">
    <div class="band band--name"></div>
    <div class="band band--phone"></div>
    <div class="panel-contact"></div>

    <h1 class="headline">
      <span class="headline__top">Corvell's Finest Realtor</span>
      <span class="headline__bottom">4 Years in a Row!</span>
    </h1>
    <div class="agent-name">Tobias Wrenfield</div>
    <div class="agent-phone">410-555-0147</div>

    <div class="agent-photo" role="img" aria-label="Portrait of the realtor in a navy suit, buttoning his jacket"></div>

    <div class="award-badge" role="img" aria-label="Award badge"></div>

    <div class="brand">
      <span class="brand__mark"></span>
      <span class="brand__name">Summit Team</span>
    </div>

    <div class="listing-fee">1.75 Listing Fee</div>
    <div class="office-phone">
      <svg viewBox="0 0 24 24" fill="none" stroke="#fff" stroke-width="2.4" stroke-linecap="round" stroke-linejoin="round"><path d="M22 16.9v3a2 2 0 0 1-2.2 2 19.8 19.8 0 0 1-8.6-3.1 19.5 19.5 0 0 1-6-6A19.8 19.8 0 0 1 2.1 4.2 2 2 0 0 1 4.1 2h3a2 2 0 0 1 2 1.7c.1 1 .4 1.9.7 2.8a2 2 0 0 1-.5 2.1L8 9.9a16 16 0 0 0 6 6l1.3-1.3a2 2 0 0 1 2.1-.4c.9.3 1.8.6 2.8.7a2 2 0 0 1 1.7 2z"/></svg>
      <span>833-555-0192</span>
    </div>
    <div class="office-address">
      <svg viewBox="0 0 24 28" fill="none" stroke="#fff" stroke-width="2.2"><path d="M12 20s7-7 7-12a7 7 0 0 0-14 0c0 5 7 12 7 12z"/><circle cx="12" cy="8" r="2.5"/><ellipse cx="12" cy="24" rx="9" ry="2.5"/></svg>
      <span>2947 W Pennlow Rd,<br>Bel Air, MD 21099</span>
    </div>
  </section>
</body>
</html>
```